website design for Kestrel Plan Studio
Kestrel Plan Studios
Well done to everyone who submitted their designs. We have selected our winner and look forward to our next project on Pixelvarnish...
Thank you very much everyone for your efforts, you have all done a great job, now we have the tough decision of deciding a winner!
Please check your private message.
please feel free to let me know the required changes so that your expectations are met.
LuroTen
Comment by DW - draft #25 and draft#40 - excellent work!
Comment by RN - draft#37 I like the top section of this page which incorporates the world map, looks good. Can we please expand it to show the southern hemispher because we are in Australia.
Cheers
Neville
Comment by RN - Draft#30 I like the layout, & I like that it contains all of the required info and looks simple, good work. Just a thought, is there a possibility of adding shimmers to give it a polished look. I notice that websites such as quindle.example do this.
Keep up the good work everyone, they all look good!
Comment by DW - I have uploaded 3 packages containing sample images that can be used on the website. Please incorporate some of them into you design. Thanks.
Command by DW - Okafor - draft #12. Like what you have done with the background image then the frame on top. We would like to go for a lighter colour scheme similar to what you have done in Draft #13.
We are off to a great start... This website needs to be more graphical than functional. It will only have a few pages with very little text. Our business is more about 3D modelling and drafting rather than construction and consulting.
HI
rN
PLEASE CHECK YOU PRIVATE MESSEGE
THANKS
Very interested to make a mock-up.
Not getting your site : http://www.kestrelplan.example.au
Also please provide your LOGO.
Thanks
Torvald

```html
<!DOCTYPE html>
<html lang="en">
<head>
<meta charset="utf-8">
<title>Kestrel Plan Studios</title>
<link rel="stylesheet" href="https://fonts.googleapis.com/css2?family=Oswald:wght@400;500&family=Arimo:wght@400;700&display=swap">
<style>
:root{
  --page:#e6e8ea;
  --white:#ffffff;
  --ink:#3a3a3a;
  --muted:#666;
  --blue:#1a6fb8;
  --blue-dark:#0c4f8c;
  --blue-light:#3d95d8;
  --cyan:#2aa9e0;
  --green:#9ccf4a;
  --hero:#1f2b35;
  --hero-2:#2c3b47;
  --footer:#1d2932;
  --footer-2:#26343f;
  --base:#121a20;
  --line:#d6d9dc;
}
*{margin:0;padding:0;box-sizing:border-box}
html,body{width:1200px;height:915px;overflow:hidden}
body{position:relative;background:var(--page);font-family:"Arimo",Arial,sans-serif;color:var(--ink);font-size:10px}
.abs{position:absolute}
.header{left:0;top:0;width:1200px;height:104px;background:linear-gradient(#f4f5f6,#dfe2e5)}
.header-panel{left:240px;top:0;width:720px;height:104px;background:linear-gradient(#ffffff,#eef0f2)}
.brand{left:250px;top:30px;display:flex;align-items:center;gap:10px}
.brand-dot{width:44px;height:44px;border-radius:50%;background:var(--blue)}
.brand-name{font-family:"Oswald",sans-serif;font-weight:500;font-size:22px;color:var(--blue);letter-spacing:.5px}
.utility{left:900px;top:12px;display:flex;gap:12px}
.utility span{width:9px;height:9px;background:#8a949c;border-radius:2px}
.support{left:790px;top:48px;width:152px;text-align:right;font-family:"Oswald",sans-serif;font-size:11px;color:var(--cyan);letter-spacing:.5px}
.phone{left:782px;top:62px;display:flex;align-items:center;gap:6px;font-family:"Oswald",sans-serif;font-size:19px;color:#1b4d7a}
.nav{left:0;top:104px;width:1200px;height:32px;background:linear-gradient(#1b76c2,#0b4c8a);border-bottom:2px solid #083a6a}
.nav ul{position:absolute;left:272px;top:9px;display:flex;gap:30px;list-style:none}
.nav li{font-size:10px;color:#fff;text-transform:uppercase}
.search{left:805px;top:111px;width:136px;height:17px;background:#fff;border-radius:9px;padding:3px 10px;color:#999;font-size:9px}
.search svg{position:absolute;right:7px;top:4px}
.hero{left:0;top:136px;width:1200px;height:272px;background:linear-gradient(90deg,var(--hero),var(--hero-2) 50%,var(--hero))}
.hero-title{left:252px;top:152px;font-family:"Oswald",sans-serif;font-weight:500;font-size:16px;line-height:23px;letter-spacing:.3px}
.hero-title .accent{color:var(--green)}
.hero-title .light{color:#fff}
.hero-copy{left:252px;top:222px;width:210px;color:#e5eaee;font-size:10px;line-height:13px}
.hero-media{left:478px;top:152px;width:462px;height:246px;border:4px solid #f0f2f4;background:linear-gradient(135deg,#e8ebee,#b8bfc6 60%,#8e979f)}
.dots{left:680px;top:374px;display:flex;gap:6px}
.dots span{width:10px;height:10px;border-radius:50%;background:#fff;opacity:.8}
.dots span:first-child{background:var(--blue);opacity:1}
.strip{left:0;top:408px;width:1200px;height:26px;background:linear-gradient(#f3f4f5,#dcdfe2)}
.cta{left:252px;top:376px;width:145px;height:30px;border-radius:15px;background:linear-gradient(var(--blue-light),var(--blue-dark));color:#fff;font-family:"Oswald",sans-serif;font-size:14px;padding:5px 0 0 14px}
.cta svg{position:absolute;right:4px;top:4px}
.content{left:240px;top:434px;width:720px;height:318px;background:var(--white)}
.welcome-icon{left:252px;top:438px;width:24px;height:24px;border-radius:50%;background:var(--blue)}
.welcome{left:282px;top:439px;font-family:"Oswald",sans-serif;font-weight:500;font-size:16px;color:#222}
.welcome b{font-weight:500;color:var(--blue)}
.intro{left:252px;width:700px;font-size:9px;line-height:12px;color:var(--muted)}
.col-title{top:544px;font-family:"Oswald",sans-serif;font-weight:500;font-size:14px;color:#222}
.col-title b{font-weight:400;color:var(--blue)}
.col-media{top:569px;width:210px;height:72px;border:1px solid #bfc5ca}
.media-project{background:linear-gradient(180deg,#f4f5f6,#c9c3ba)}
.media-service{background:linear-gradient(180deg,#d9dcde,#8c9299)}
.col-copy{top:651px;width:212px;font-size:9.5px;line-height:12px;color:#444}
.news{left:737px;width:212px}
.news-date{display:flex;align-items:center;gap:7px;font-weight:700;font-size:10px;color:#222;margin-bottom:4px}
.news-text{font-size:9.5px;line-height:12px;color:#444}
.read{top:713px;font-size:9px;color:var(--blue)}
.rule{left:252px;top:728px;width:696px;height:1px;background:var(--line)}
.footer{left:0;top:752px;width:1200px;height:114px;background:linear-gradient(var(--footer-2),var(--footer))}
.foot-title{top:766px;font-family:"Oswald",sans-serif;font-weight:500;font-size:14px;color:var(--cyan)}
.foot-links{top:790px;display:grid;grid-template-columns:70px 70px;font-size:9px;line-height:20px;color:#d8dde1}
.foot-address{left:472px;top:790px;font-size:9px;line-height:20px;color:#d8dde1}
.foot-contact{left:567px;top:790px;display:grid;grid-template-columns:38px 150px;font-size:9px;line-height:20px;color:#d8dde1}
.social{left:806px;top:796px;display:flex;gap:14px}
.social span{width:40px;height:40px;border-radius:50%;background:linear-gradient(#5a8fd0,#2d5fa0);border:2px solid #cfd8e0}
.social span + span{background:linear-gradient(#6ad0f2,#2aa0d6)}
.base{left:0;top:866px;width:1200px;height:49px;background:var(--base);color:#cfd4d8;font-size:9px;text-align:center;padding-top:20px}
</style>
</head>
<body>
<div class="abs header"></div>
<div class="abs header-panel"></div>
<div class="abs brand"><span class="brand-dot"></span><span class="brand-name">Kestrel Plan Studios</span></div>
<div class="abs utility"><span></span><span></span><span></span></div>
<div class="abs support">ONLINE SUPPORT!</div>
<div class="abs phone">
  <svg width="18" height="18" viewBox="0 0 24 24"><circle cx="12" cy="12" r="12" fill="#2aa9e0"/><path d="M8 6l2.5 0 1 3-1.5 1.2c.8 1.6 2 2.8 3.6 3.6L14.8 12.3l3 1v2.5c-5.5 0-9.8-4.3-9.8-9.8z" fill="#fff"/></svg>
  <span>+61.888.8888.888</span>
</div>

<nav class="abs nav">
  <ul><li>Home</li><li>About Us</li><li>Services</li><li>Projects</li><li>News</li><li>Contact Us</li></ul>
</nav>
<div class="abs search">Search...
  <svg width="9" height="9" viewBox="0 0 10 10"><circle cx="4" cy="4" r="3" fill="none" stroke="#1a6fb8" stroke-width="1.5"/><path d="M6.3 6.3L9 9" stroke="#1a6fb8" stroke-width="1.5"/></svg>
</div>

<section class="abs hero"></section>
<h1 class="abs hero-title"><span class="accent">LOREM IPSUM DOLOR SIT AMET,</span><br><span class="light">CONSECTETUR ADIPISCING ELIT</span></h1>
<p class="abs hero-copy">Lorem ipsum dolor sit amet, consectetur adipiscing elit, sed do eiusmod tempor incididunt ut labore et dolore magna aliqua. Ut enim ad minim veniam quis nostrud.</p>
<div class="abs hero-media" role="img" aria-label="Slideshow photo of architectural drawings with drafting tools and pencils"></div>
<div class="abs dots"><span></span><span></span><span></span><span></span></div>
<div class="abs strip"></div>
<div class="abs cta">LEARN MORE
  <svg width="22" height="22" viewBox="0 0 22 22"><circle cx="11" cy="11" r="11" fill="#fff"/><path d="M8 6l6 5-6 5z" fill="#1a6fb8"/></svg>
</div>

<main class="abs content"></main>
<div class="abs welcome-icon"></div>
<h2 class="abs welcome">WELCOME TO <b>KESTREL PLAN STUDIOS</b></h2>
<p class="abs intro" style="top:468px">Lorem ipsum dolor sit amet, consectetur adipiscing elit, sed do eiusmod tempor incididunt ut labore et dolore magna aliqua. Ut enim ad minim veniam, quis nostrud exercitation ullamco laboris nisi ut aliquip ex ea commodo consequat. Duis aute irure dolor in reprehenderit in voluptate velit esse cillum dolore eu fugiat nulla pariatur. Excepteur sint occaecat cupidatat.</p>
<p class="abs intro" style="top:512px">Lorem ipsum dolor sit amet, consectetur adipiscing elit, sed do eiusmod tempor incididunt ut labore et dolore magna aliqua.</p>

<h3 class="abs col-title" style="left:252px">CURRENT <b>PROJECTS</b></h3>
<div class="abs col-media media-project" style="left:252px" role="img" aria-label="Sketch of a timber-framed building under construction"></div>
<p class="abs col-copy" style="left:252px">Lorem ipsum dolor sit amet, consectetur adipiscing elit, sed do eiusmod tempor incididunt ut labore et dolore magna aliqua. Ut enim ad minim veniam, quis nostrud.</p>
<span class="abs read" style="left:410px">[Read More]</span>

<h3 class="abs col-title" style="left:494px">OUR <b>SERVICES</b></h3>
<div class="abs col-media media-service" style="left:494px" role="img" aria-label="Drawing of a classical building facade with columns"></div>
<p class="abs col-copy" style="left:494px">Lorem ipsum dolor sit amet, consectetur adipiscing elit, sed do eiusmod tempor incididunt ut labore et dolore magna aliqua. Ut enim ad minim veniam, quis nostrud.</p>
<span class="abs read" style="left:652px">[Read More]</span>

<h3 class="abs col-title" style="left:737px">LATEST <b>NEWS</b></h3>
<div class="abs news" style="top:573px">
  <div class="news-date"><svg width="12" height="12" viewBox="0 0 12 12"><rect x="0.5" y="1.5" width="11" height="10" fill="#fff" stroke="#c0392b"/><rect x="0.5" y="1.5" width="11" height="3" fill="#c0392b"/></svg>10-5-2011</div>
  <p class="news-text">Lorem ipsum dolor sit amet, consectetur adipiscing elit sed do eiusmod.</p>
</div>
<div class="abs news" style="top:627px">
  <div class="news-date"><svg width="12" height="12" viewBox="0 0 12 12"><rect x="0.5" y="1.5" width="11" height="10" fill="#fff" stroke="#c0392b"/><rect x="0.5" y="1.5" width="11" height="3" fill="#c0392b"/></svg>10-5-2011</div>
  <p class="news-text">Lorem ipsum dolor sit amet, consectetur adipiscing elit sed do eiusmod.</p>
</div>
<span class="abs read" style="left:896px">[Read More]</span>
<div class="abs rule"></div>

<footer class="abs footer"></footer>
<h4 class="abs foot-title" style="left:252px">NAVIGATION</h4>
<div class="abs foot-links" style="left:256px"><span>Home</span><span>News</span><span>About us</span><span>Sitemap</span><span>Services</span><span>Contact Us</span><span>Projects</span></div>
<h4 class="abs foot-title" style="left:470px">CONTACT US</h4>
<div class="abs foot-address">Address line 1<br>Address line 2<br>City, State,<br>Country.</div>
<div class="abs foot-contact"><span>Phone :</span><span>+61.888.8888.888</span><span>Fax :</span><span>+61.888.8888.888</span><span>Email :</span><span>info@kestrelplan.example.au</span></div>
<h4 class="abs foot-title" style="left:806px">FOLLOW US</h4>
<div class="abs social" role="img" aria-label="Social network links"><span></span><span></span></div>
<div class="abs base">Copyright © 2011 Kestrel Plan Studios. All Rights Reserved.</div>
</body>
</html>
```